Mental Health care Company in Washington DC

We are a new mental health care services provider in Washington DC. Please look at these sites.
https://marlowbrookpartners.com
https://www.quillstoneinc.com
https://velmarsh-kt.org/
https://www.trivanqx.com
https://www.thelanternofqz.com

```html
<!DOCTYPE html>
<html lang="en">
<head>
<meta charset="utf-8">
<title>Veyra Health – Mental Health Care in Washington, DC</title>
<link rel="stylesheet" href="https://fonts.googleapis.com/css2?family=Outfit:wght@400;500;600;700&family=Montserrat:wght@400;500;600;700&display=swap">
<style>
:root{
  --orange:#f5821f;
  --orange-soft:#f79a45;
  --ink:#2e2e2e;
  --grey:#8a8a8a;
  --light:#f3f3f3;
  --teal:#9fd8dc;
  --white:#ffffff;
  --page-bg:#eeeeee;
}
*{box-sizing:border-box;margin:0;padding:0}
html,body{width:1200px;height:4354px;overflow:hidden;background:var(--page-bg)}
body{font-family:"Montserrat",sans-serif;color:var(--ink)}
.site{position:absolute;left:84px;top:0;width:1033px;height:4354px;background:var(--white);box-shadow:0 0 24px rgba(0,0,0,.12);overflow:hidden}
.abs{position:absolute}
h1,h2,h3,.heading{font-family:"Outfit",sans-serif;font-weight:600;color:#3a3a3a;letter-spacing:-.5px}

/* header */
.brand{left:73px;top:20px;font-family:"Outfit",sans-serif;font-size:30px;font-weight:600;color:#2a4a70}
.nav{top:0;height:83px;display:flex;align-items:center;font-size:13px;font-weight:500;color:#222}
.nav-home{left:496px;top:0;width:79px;height:83px;background:var(--teal);display:flex;align-items:center;justify-content:center;font-size:13px;font-weight:500}
.nav-link{top:40px;font-size:13px;font-weight:500}

/* hero */
.hero{left:0;top:83px;width:1033px;height:416px;background:linear-gradient(100deg,#1c140f 0%,#3b2a22 35%,#6a4a3a 60%,#2c2623 100%)}
.hero-title{left:85px;top:140px;font-family:"Outfit",sans-serif;font-weight:700;font-size:42px;line-height:49px;color:var(--orange)}
.hero-sub{left:82px;top:300px;width:560px;font-size:15px;line-height:20px;color:#f2f2f2}
.btn{background:var(--orange);color:var(--white);display:flex;align-items:center;justify-content:center;font-family:"Montserrat",sans-serif;font-weight:600}
.hero-btn{left:685px;top:297px;width:223px;height:46px;font-size:19px;font-weight:500}

/* contact band */
.band{left:0;top:499px;width:1033px;height:106px;background:var(--orange);color:var(--white)}
.band-item{top:24px}
.band-item strong{display:block;font-family:"Outfit",sans-serif;font-size:21px;font-weight:500}
.band-item span{display:block;font-size:11px;font-weight:700;margin-top:4px}
.band-div{top:28px;width:1px;height:44px;background:rgba(255,255,255,.6)}

/* about */
.sq{background:var(--orange)}
.photo{border-radius:0}
.eyebrow{color:var(--orange);font-family:"Outfit",sans-serif;font-weight:500}
.about-eyebrow{left:87px;top:810px;font-size:25px}
.section-title{font-size:42px;line-height:49px}
.about-title{left:82px;top:866px}
.body-copy{color:var(--grey);font-size:16px;line-height:20px}
.about-copy{left:82px;top:994px;width:880px}

/* services */
.services-title{left:0;width:1013px;top:1160px;text-align:center}
.services-sub{left:0;width:1013px;top:1224px;text-align:center;font-size:16px}
.card{top:1323px;width:253px;height:311px;background:var(--white);box-shadow:0 2px 14px rgba(0,0,0,.14)}
.card-photo{position:absolute;left:0;top:0;width:253px;height:156px}
.card-icon{position:absolute;left:92px;top:122px;width:68px;height:68px;border-radius:50%;background:#ececec;border:4px solid #fff;display:flex;align-items:center;justify-content:center}
.card h3{position:absolute;left:0;width:100%;top:200px;text-align:center;font-family:"Montserrat",sans-serif;font-size:15px;font-weight:700;color:#111;letter-spacing:0}
.card p{position:absolute;left:0;width:100%;top:227px;text-align:center;font-size:13px;line-height:17px;color:#333}
.card .btn{position:absolute;left:77px;top:276px;width:99px;height:22px;font-size:12px}
.services-copy{left:0;width:1033px;top:1688px;text-align:center;font-size:14px;line-height:21px}
.services-btn{left:457px;top:1759px;width:147px;height:29px;font-size:14px}

/* why */
.why-bg{left:180px;top:1960px;width:680px;height:520px;background:radial-gradient(ellipse at center,#ffffff 20%,#f1f1f1 55%,#ffffff 75%)}
.why-eyebrow{left:0;width:1033px;top:1860px;text-align:center;font-size:16px}
.why-title{left:0;width:1033px;top:1890px;text-align:center;line-height:45px;font-size:40px}
.mind{left:416px;top:2011px;width:232px;height:304px;border-radius:48% 46% 30% 40%/40% 44% 30% 30%;background:linear-gradient(180deg,#8fb1d4 0%,#e7b357 45%,#c27a1e 62%,#4d6a25 100%)}
.value{width:200px}
.value .vsq{position:absolute;left:-38px;top:4px;width:15px;height:15px;background:var(--orange)}
.value h4{font-family:"Outfit",sans-serif;font-weight:400;font-size:18px;color:#444}
.value p{font-size:9px;line-height:11px;color:#999;margin-top:6px}
.why-btn{left:479px;top:2395px;width:145px;height:44px;font-size:15px}

/* team */
.team-eyebrow{left:636px;top:2553px;font-size:19px;font-weight:600}
.team-title{left:93px;top:2597px;line-height:49px}
.team-copy{left:98px;top:2814px;width:420px;font-size:11px;line-height:14px;color:#333}
.therapist{width:161px;height:290px;border:2px solid #a6dde0;background:linear-gradient(180deg,#e9edf0,#c9ccd0)}
.therapist .cap{position:absolute;left:16px;bottom:16px;width:135px;color:var(--white);font-size:11px;line-height:14px}
.therapist .cap b{display:block;margin-bottom:6px}

/* testimonials */
.test-eyebrow{left:300px;top:3005px;font-size:16px}
.test-title{left:300px;top:3036px;font-size:40px}
.tcard{background:var(--white);box-shadow:0 2px 14px rgba(0,0,0,.14)}
.avatar{position:absolute;border-radius:50%;background:#c9bcb2}
.tname{position:absolute;font-size:11px;line-height:13px;color:#333}
.tquote{position:absolute;font-size:11px;line-height:13px;color:#999}
.stars{position:absolute;color:#f3c245;font-size:17px;letter-spacing:1px}
.tline{left:632px;top:3127px;width:1px;height:299px;background:var(--orange)}

/* cta form */
.cta-title{left:82px;top:3540px;line-height:49px}
.flabel{left:86px;font-size:20px;color:#333}
.finput{left:185px;width:306px;border:1px solid #9a9a9a;background:var(--white)}
.send{left:342px;top:3889px;width:149px;height:33px;font-size:19px;font-weight:500}

/* footer */
.fnav{top:4046px;font-size:13px;font-weight:600;color:#111}
.flogo{left:82px;top:4080px;font-family:"Outfit",sans-serif;font-size:46px;font-weight:600;color:#2a4a70}
.fnote{left:82px;top:4172px;font-size:13px;line-height:17px;color:#666}
.social{top:4228px;width:20px;height:20px;border-radius:50%;background:var(--orange)}
.fcontact{top:4231px;font-size:12px;color:#333}
.copy-band{left:0;top:4276px;width:1033px;height:78px;background:var(--orange);color:var(--white);font-size:11px;display:flex;align-items:center;justify-content:center}
</style>
</head>
<body>
<div class="site">

  <!-- header -->
  <div class="abs brand">Veyra Health</div>
  <div class="abs nav-home">Home</div>
  <div class="abs nav-link" style="left:612px">About</div>
  <div class="abs nav-link" style="left:692px">Services</div>
  <div class="abs nav-link" style="left:781px">Therapists</div>
  <div class="abs nav-link" style="left:871px">Resources</div>
  <div class="abs nav-link" style="left:957px">Contact</div>

  <!-- hero -->
  <div class="abs hero" role="img" aria-label="Photo of a smiling therapist and client during a session"></div>
  <h1 class="abs hero-title">Your Mental<br>Wellness<br>Starts Here</h1>
  <p class="abs hero-sub">Compassionate, personalized mental health care for individuals, couples, and families. In-office and virtual therapy available.</p>
  <div class="abs btn hero-btn">Get a Appoinment</div>

  <!-- contact band -->
  <div class="abs band">
    <div class="abs band-item" style="left:85px"><strong>0800 555&nbsp; 01 234</strong><span>For a free consultation</span></div>
    <div class="abs band-div" style="left:360px"></div>
    <div class="abs band-item" style="left:474px"><strong>chat whith us</strong><span>for more details</span></div>
    <div class="abs band-div" style="left:744px"></div>
    <div class="abs band-item" style="left:785px"><strong>24/7 support</strong><span>for more details</span></div>
  </div>

  <!-- about -->
  <div class="abs sq" style="left:283px;top:666px;width:145px;height:106px"></div>
  <div class="abs sq" style="left:371px;top:703px;width:155px;height:128px;border-left:6px solid #fff;border-top:6px solid #fff"></div>
  <div class="abs sq" style="left:896px;top:909px;width:118px;height:88px"></div>
  <div class="abs photo" style="left:541px;top:703px;width:389px;height:250px;background:linear-gradient(160deg,#d9dde0,#8d8f93 55%,#3a3c40)" role="img" aria-label="Photo of a cheerful team gathered around a laptop in an office"></div>
  <div class="abs eyebrow about-eyebrow">About us</div>
  <h2 class="abs section-title about-title">Therapy That Meets<br>&nbsp;You Where You Are</h2>
  <p class="abs body-copy about-copy">At Veyra Health, we provide modern, science-backed mental health services with a human touch. Located in the heart of Washington, DC, our licensed therapists are dedicated to helping you find balance, clarity, and strength through life's challenges.</p>

  <!-- services -->
  <h2 class="abs section-title services-title">Our Services</h2>
  <div class="abs eyebrow services-sub">Therapy That Meets You Where You Are</div>

  <div class="abs card" style="left:82px">
    <div class="card-photo" role="img" aria-label="Photo of a therapist comforting a client" style="background:linear-gradient(135deg,#e8e4df,#b59a86)"></div>
    <div class="card-icon"><svg width="34" height="34" viewBox="0 0 34 34" fill="none" stroke="#666" stroke-width="2"><circle cx="17" cy="17" r="15"/><path d="M11 20c-2-1-2-5 0-6 0-3 4-4 6-2 2-2 6-1 6 2 2 1 2 5 0 6 0 2-3 3-5 2h-2c-2 1-5 0-5-2z"/><path d="M17 12v10"/></svg></div>
    <h3>Lorem ipsum dolor</h3>
    <p>consectetur adipiscing elit,<br>sed do eiusmod tempor</p>
    <div class="btn">View All</div>
  </div>
  <div class="abs card" style="left:384px">
    <div class="card-photo" role="img" aria-label="Photo of an older man and a young woman giving a high five" style="background:linear-gradient(135deg,#f1efe9,#c5c0b6)"></div>
    <div class="card-icon"><svg width="34" height="34" viewBox="0 0 34 34" fill="none" stroke="#666" stroke-width="2"><circle cx="17" cy="17" r="15"/><path d="M11 20c-2-1-2-5 0-6 0-3 4-4 6-2 2-2 6-1 6 2 2 1 2 5 0 6 0 2-3 3-5 2h-2c-2 1-5 0-5-2z"/><path d="M17 12v10"/></svg></div>
    <h3>Lorem ipsum dolor</h3>
    <p>consectetur adipiscing elit,<br>sed do eiusmod tempor</p>
    <div class="btn">View All</div>
  </div>
  <div class="abs card" style="left:687px">
    <div class="card-photo" role="img" aria-label="Photo of two men sharing a warm hug" style="background:linear-gradient(135deg,#d8d2ca,#8c8077)"></div>
    <div class="card-icon"><svg width="34" height="34" viewBox="0 0 34 34" fill="none" stroke="#666" stroke-width="2"><circle cx="17" cy="17" r="15"/><path d="M11 20c-2-1-2-5 0-6 0-3 4-4 6-2 2-2 6-1 6 2 2 1 2 5 0 6 0 2-3 3-5 2h-2c-2 1-5 0-5-2z"/><path d="M17 12v10"/></svg></div>
    <h3>Lorem ipsum dolor</h3>
    <p>consectetur adipiscing elit,<br>sed do eiusmod tempor</p>
    <div class="btn">View All</div>
  </div>

  <p class="abs body-copy services-copy">At Veyra Health, we provide modern, science-backed mental health services with a human touch.<br>Located in the heart of Washington, DC, our licensed therapists are dedicated to</p>
  <div class="abs btn services-btn">View All</div>

  <!-- why choose us -->
  <div class="abs why-bg"></div>
  <div class="abs eyebrow why-eyebrow">Why choose Us</div>
  <h2 class="abs why-title">Mental wellness<br>starts here</h2>
  <div class="abs mind" role="img" aria-label="Illustration of a head silhouette filled with a tree at sunset"></div>

  <div class="abs value" style="left:149px;top:2046px"><span class="vsq"></span><h4>Value one</h4><p>Calm, caring support shaped around your goals and daily life.</p></div>
  <div class="abs value" style="left:138px;top:2166px"><span class="vsq" style="left:-27px"></span><h4>Value three</h4><p>Calm, caring support shaped around your goals and daily life.</p></div>
  <div class="abs value" style="left:149px;top:2271px"><span class="vsq"></span><h4>Value one</h4><p>Calm, caring support shaped around your goals and daily life.</p></div>
  <div class="abs value" style="left:778px;top:2029px"><span class="vsq"></span><h4>Value two</h4><p>Calm, caring support shaped around your goals and daily life.</p></div>
  <div class="abs value" style="left:778px;top:2150px"><span class="vsq"></span><h4>Value four</h4><p>Calm, caring support shaped around your goals and daily life.</p></div>
  <div class="abs value" style="left:780px;top:2254px"><span class="vsq" style="left:-40px"></span><h4>Value one</h4><p>Calm, caring support shaped around your goals and daily life.</p></div>
  <div class="abs btn why-btn">Contact us</div>

  <!-- therapists -->
  <div class="abs eyebrow team-eyebrow">Meet Our Therapists</div>
  <h2 class="abs section-title team-title">A Team<br>That Listens,<br>Understands,<br>and Supports</h2>
  <p class="abs team-copy">At Veyra Health, we provide modern, science-backed mental health services with a human touch. Located in the heart of Washington, DC, our licensed therapists</p>

  <div class="abs therapist" style="left:469px;top:2603px" role="img" aria-label="Photo of a therapist in a white coat">
    <div class="cap"><b>Lorem ipsum</b>Lorem ipsum dolor sit amet, consectetur adipiscing elit, sed do eiusmod tempor</div>
  </div>
  <div class="abs therapist" style="left:643px;top:2638px;background:linear-gradient(180deg,#eceeef,#a9a39c)" role="img" aria-label="Photo of a smiling therapist in a grey blazer">
    <div class="cap"><b>Lorem ipsum</b>Lorem ipsum dolor sit amet, consectetur adipiscing elit, sed do eiusmod tempor</div>
  </div>
  <div class="abs therapist" style="left:820px;top:2603px;background:linear-gradient(180deg,#eef0f2,#2e3347 70%)" role="img" aria-label="Photo of a therapist in a navy sweater">
    <div class="cap"><b>Lorem ipsum</b>Lorem ipsum dolor sit amet, consectetur adipiscing elit, sed do eiusmod tempor</div>
  </div>

  <!-- testimonials -->
  <div class="abs eyebrow test-eyebrow">Testimonials</div>
  <h2 class="abs test-title">What Our Clients Say</h2>

  <div class="abs tcard" style="left:119px;top:3147px;width:461px;height:240px">
    <div class="avatar" role="img" aria-label="Client portrait" style="left:28px;top:36px;width:44px;height:44px"></div>
    <div class="tname" style="left:88px;top:48px">Marco Delgado<br>Location: Madrid, Spain</div>
    <div class="tquote" style="left:70px;top:116px;width:340px">At Veyra Health, they provide modern, science-backed mental health services with a human touch. Located in the heart of Washington, DC, our licensed therapists At Veyra Health, they provide modern, science-backed mental health services with a human touch. Located in the heart of Washington, DC, our licensed therapists</div>
    <div class="stars" style="left:64px;top:200px">★★★★★</div>
  </div>

  <div class="abs tline"></div>

  <div class="abs tcard" style="left:678px;top:3128px;width:230px;height:129px">
    <div class="avatar" role="img" aria-label="Client portrait" style="left:16px;top:14px;width:38px;height:38px"></div>
    <div class="tname" style="left:64px;top:24px;font-size:10px">Anika Rao<br>Location: Pune</div>
    <div class="tquote" style="left:26px;top:78px;width:190px;font-size:10px">At Veyra Health, they provide modern, health services with a human touch.</div>
    <div class="stars" style="left:60px;top:100px;font-size:15px">★★★★★</div>
  </div>
  <div class="abs tcard" style="left:678px;top:3275px;width:230px;height:127px">
    <div class="avatar" role="img" aria-label="Client portrait" style="left:16px;top:14px;width:38px;height:38px"></div>
    <div class="tname" style="left:64px;top:26px;font-size:10px">Owen Hartley<br>Location: Madrid, Spain</div>
    <div class="tquote" style="left:26px;top:78px;width:190px;font-size:10px">At Veyra Health, they provide modern, health services with a human touch.</div>
    <div class="stars" style="left:60px;top:100px;font-size:15px">★★★★★</div>
  </div>

  <!-- call to action form -->
  <h2 class="abs section-title cta-title">Ready to Begin<br>Your Healing Journey?</h2>
  <div class="abs flabel" style="top:3687px">Name</div>
  <div class="abs flabel" style="top:3736px">Email</div>
  <div class="abs flabel" style="left:82px;top:3785px">Content</div>
  <div class="abs finput" style="top:3681px;height:34px"></div>
  <div class="abs finput" style="top:3731px;height:34px"></div>
  <div class="abs finput" style="top:3786px;height:84px"></div>
  <div class="abs btn send">Send</div>

  <svg class="abs" style="left:639px;top:3600px" width="260" height="310" viewBox="0 0 260 310" fill="none" stroke="#f5821f" stroke-width="2">
    <path d="M0 30V0h60"/><path d="M255 250v58h-60"/>
  </svg>
  <div class="abs" style="left:655px;top:3568px;width:218px;height:322px;background:linear-gradient(180deg,#f0f0f0,#b78459 60%,#6b4a33)" role="img" aria-label="Photo of two smiling men, one pointing forward"></div>
  <div class="abs" style="left:908px;top:3612px;width:125px;height:236px;background:linear-gradient(180deg,#d7d2cb,#4d5566)" role="img" aria-label="Photo of an older man in conversation"></div>

  <!-- footer -->
  <div class="abs fnav" style="left:548px">About</div>
  <div class="abs fnav" style="left:636px">Services</div>
  <div class="abs fnav" style="left:729px">Careers</div>
  <div class="abs fnav" style="left:815px">Blog</div>
  <div class="abs fnav" style="left:884px">Privacy Policy</div>

  <div class="abs flogo">Veyra Health</div>
  <p class="abs fnote">Our latest news and important announcecf.<br>Our latest news and important.</p>
  <div class="abs social" style="left:114px" aria-label="Social link"></div>
  <div class="abs social" style="left:143px" aria-label="Social link"></div>
  <div class="abs social" style="left:171px" aria-label="Social link"></div>

  <svg class="abs" style="left:638px;top:4228px" width="22" height="22" viewBox="0 0 22 22"><circle cx="11" cy="11" r="11" fill="#f5821f"/><path d="M7 6l2-1 2 3-1.5 1.5c.7 1.5 1.6 2.4 3 3L14 11l3 2-1 2c-4 0-9-5-9-9z" fill="#fff"/></svg>
  <div class="abs fcontact" style="left:672px">(202) 555-0147</div>
  <svg class="abs" style="left:809px;top:4228px" width="22" height="22" viewBox="0 0 22 22"><circle cx="11" cy="11" r="11" fill="#f5821f"/><rect x="5.5" y="7" width="11" height="8" fill="none" stroke="#fff" stroke-width="1.4"/><path d="M5.5 7l5.5 4.5L16.5 7" fill="none" stroke="#fff" stroke-width="1.4"/></svg>
  <div class="abs fcontact" style="left:840px">hello@veyrahealthdc.com</div>

  <div class="abs copy-band">© 2025 Veyra Health. All Rights Reserved.</div>
</div>
</body>
</html>
```